Baby Care Print Log for Nannies and Parents- Creating a brand/style I can use across different forms

I am creating a notebook for babysitters to use to communicate with parents about the children they care for. I will be creating many different forms (emergency contacts, daily logs, shopping lists, etc.)
I need a look and feel from which to style these forms from. I am starting by designing the daily baby care log. I need a designer to take my Word doc with just text on it, and create a visual approach to make this visually appealing.
I do not want this to be extremely "babyish" with cartoon styling. I want it to be more of a professional looking style. I would like to be able to color each different document a different color palette, yet keep the similar look and feel. My logo is attached for inspiration. I use real photography across my website velmorapath.com.
Updates
I will be re-designing my Wordpress website based on what design I like best and also will need other forms completed once I pick a design. I am hoping to work with someone who I can hire for further development needs as well. Added Saturday, February 11, 2017
Target Market(s)
Professional Parents
Industry/Entity Type
Education
Requirements
Must have
- color, pop, visual appeal
- Please use the color in my logo and any complementary colors that you think work well with it. I definitely like colored patterns, ombre, colored backgrounds, etc. I'd prefer for it not to be completely white with only pops of color here and there.
Nice to have
- My logo somewhere subtly on the form
- Photography elements
Should not have
- cartoon images of babies, etc. I use real photography across my website with the exception of my logo umbrella.

```html
<!DOCTYPE html>
<html lang="en">
<head>
<meta charset="utf-8">
<title>Velmora Path – Daily Baby Care Log</title>
<link href="https://fonts.googleapis.com/css2?family=Lato:wght@400;700;900&display=swap" rel="stylesheet">
<style>
:root{
  --sea:#12c3dd;
  --sea-soft:#3fd3e2;
  --band:#63d8da;
  --band-edge:#2fbfc7;
  --mint:#b2ead3;
  --tab:#e6fbf1;
  --field:#e0fdfc;
  --field-line:#5fb1aa;
  --rule:#bfe3e3;
  --check:#5bd5cf;
  --ink:#1d2a2a;
  --arrow:#16b9d6;
}
*{box-sizing:border-box;margin:0;padding:0}
html,body{width:927px;height:1200px;overflow:hidden}
body{font-family:"Lato",sans-serif;color:var(--ink);
  background:linear-gradient(160deg,var(--sea-soft) 0%,var(--sea) 55%,#0bbfd9 100%);position:relative}
.band{position:absolute;top:0;height:1200px;background:var(--band)}
.band-left{left:76px;width:44px;border-right:8px solid var(--band-edge)}
.band-right{left:806px;width:44px;border-left:8px solid var(--band-edge)}
.sheet{position:absolute;left:120px;top:0;width:686px;height:1200px;background:var(--mint)}
.tab{position:absolute;left:358px;width:208px;background:var(--tab);box-shadow:0 4px 12px rgba(0,0,0,.12)}
.tab-top{top:0;height:132px;border-radius:0 0 34px 34px;display:flex;align-items:center;justify-content:center}
.tab-bottom{top:1162px;height:50px;border-radius:34px 34px 0 0}
.brand{font-weight:700;font-size:20px;color:#0e8fa6;display:flex;align-items:center;gap:8px}
.brand-dot{width:12px;height:12px;border-radius:50%;background:var(--sea)}
.abs{position:absolute;line-height:1}
.label{font-size:16px;font-weight:400}
.heading{font-size:16px;font-weight:900}
.field{position:absolute;background:var(--field);border:3px solid var(--field-line);border-radius:20px}
.panel{position:absolute;background:var(--field);border:3px solid var(--field-line);border-radius:32px}
.rule{position:absolute;height:1px;background:var(--rule)}
.check{position:absolute;width:29px;height:26px;border-radius:10px;background:var(--check)}
.supply{font-size:16px;display:flex;align-items:center;gap:3px}
.notes-rule{position:absolute;left:165px;width:601px;height:1px;background:#8fbdb0}
</style>
</head>
<body>
<div class="band band-left"></div>
<div class="band band-right"></div>
<div class="sheet"></div>

<div class="tab tab-top"><div class="brand"><span class="brand-dot"></span>Velmora Path</div></div>
<div class="tab tab-bottom"></div>

<div class="abs label" style="left:146px;top:158px">NameDate</div>
<div class="field" style="left:148px;top:178px;width:357px;height:37px"></div>

<div class="abs label" style="left:146px;top:231px">Nan TimeFeeding</div>
<div class="field" style="left:148px;top:252px;width:122px;height:38px"></div>

<section class="panel" style="left:146px;top:302px;width:636px;height:236px"></section>
<div class="abs heading" style="left:188px;top:329px">TimeHow LongTimeMilk(Type)</div>
<div class="abs heading" style="left:467px;top:329px">Water</div>
<div class="abs heading" style="left:565px;top:329px">Food</div>
<div class="abs heading" style="left:650px;top:329px">Amount</div>
<div class="rule" style="left:182px;top:391px;width:244px"></div><div class="rule" style="left:458px;top:391px;width:66px"></div><div class="rule" style="left:550px;top:391px;width:67px"></div><div class="rule" style="left:648px;top:391px;width:66px"></div>
<div class="rule" style="left:182px;top:426px;width:244px"></div><div class="rule" style="left:458px;top:426px;width:66px"></div><div class="rule" style="left:550px;top:426px;width:67px"></div><div class="rule" style="left:648px;top:426px;width:66px"></div>
<div class="rule" style="left:182px;top:460px;width:244px"></div><div class="rule" style="left:458px;top:460px;width:66px"></div><div class="rule" style="left:550px;top:460px;width:67px"></div><div class="rule" style="left:648px;top:460px;width:66px"></div>
<div class="rule" style="left:182px;top:494px;width:244px"></div><div class="rule" style="left:458px;top:494px;width:66px"></div><div class="rule" style="left:550px;top:494px;width:67px"></div><div class="rule" style="left:648px;top:494px;width:66px"></div>

<section class="panel" style="left:142px;top:547px;width:643px;height:306px"></section>
<div class="abs heading" style="left:164px;top:572px">DiapersMood</div>
<div class="abs heading" style="left:164px;top:604px">TimeWetBMHappy</div>
<div class="abs heading" style="left:334px;top:604px">Sad</div>
<div class="abs heading" style="left:385px;top:604px">Unsettled</div>
<div class="abs heading" style="left:468px;top:604px">Energetic</div>
<div class="abs heading" style="left:560px;top:604px">Tired</div>
<div class="abs heading" style="left:634px;top:604px">Chatty</div>
<div class="abs heading" style="left:711px;top:604px">Quiet</div>

<div class="rule" style="left:166px;top:652px;width:140px"></div>
<div class="rule" style="left:166px;top:686px;width:140px"></div>
<div class="rule" style="left:166px;top:720px;width:140px"></div>
<div class="rule" style="left:166px;top:754px;width:140px"></div>
<div class="rule" style="left:166px;top:788px;width:140px"></div>
<div class="rule" style="left:166px;top:822px;width:140px"></div>

<div class="check" style="left:334px;top:626px"></div><div class="check" style="left:409px;top:626px"></div><div class="check" style="left:491px;top:626px"></div><div class="check" style="left:566px;top:626px"></div><div class="check" style="left:644px;top:626px"></div><div class="check" style="left:720px;top:626px"></div>
<div class="check" style="left:334px;top:660px"></div><div class="check" style="left:409px;top:660px"></div><div class="check" style="left:491px;top:660px"></div><div class="check" style="left:566px;top:660px"></div><div class="check" style="left:644px;top:660px"></div><div class="check" style="left:720px;top:660px"></div>
<div class="check" style="left:334px;top:694px"></div><div class="check" style="left:409px;top:694px"></div><div class="check" style="left:491px;top:694px"></div><div class="check" style="left:566px;top:694px"></div><div class="check" style="left:644px;top:694px"></div><div class="check" style="left:720px;top:694px"></div>
<div class="check" style="left:334px;top:728px"></div><div class="check" style="left:409px;top:728px"></div><div class="check" style="left:491px;top:728px"></div><div class="check" style="left:566px;top:728px"></div><div class="check" style="left:644px;top:728px"></div><div class="check" style="left:720px;top:728px"></div>
<div class="check" style="left:334px;top:761px"></div><div class="check" style="left:409px;top:761px"></div><div class="check" style="left:491px;top:761px"></div><div class="check" style="left:566px;top:761px"></div><div class="check" style="left:644px;top:761px"></div><div class="check" style="left:720px;top:761px"></div>
<div class="check" style="left:334px;top:796px"></div><div class="check" style="left:409px;top:796px"></div><div class="check" style="left:491px;top:796px"></div><div class="check" style="left:566px;top:796px"></div><div class="check" style="left:644px;top:796px"></div><div class="check" style="left:720px;top:796px"></div>

<div class="abs heading" style="left:157px;top:876px">Today Activities</div>
<div class="field" style="left:299px;top:867px;width:475px;height:35px"></div>

<div class="abs heading" style="left:156px;top:917px">Supplies Needed Soon</div>
<div class="abs supply" style="left:155px;top:945px"><svg width="12" height="12" viewBox="0 0 12 12"><path d="M1 2 L11 6 L1 10 L4 6 Z" fill="var(--arrow)"/></svg>DiapersMilk/FormulaWet Wipes</div>
<div class="abs supply" style="left:155px;top:979px"><svg width="12" height="12" viewBox="0 0 12 12"><path d="M1 2 L11 6 L1 10 L4 6 Z" fill="var(--arrow)"/></svg>Diaper CreamCerealBaby Food</div>
<div class="abs supply" style="left:155px;top:1014px"><svg width="12" height="12" viewBox="0 0 12 12"><path d="M1 2 L11 6 L1 10 L4 6 Z" fill="var(--arrow)"/></svg>Other:</div>
<div class="field" style="left:226px;top:1004px;width:548px;height:35px"></div>

<div class="abs heading" style="left:164px;top:1047px">Special Notes</div>
<div class="notes-rule" style="top:1086px"></div>
<div class="notes-rule" style="top:1106px"></div>
<div class="notes-rule" style="top:1125px"></div>
<div class="notes-rule" style="top:1144px"></div>
</body>
</html>
```